Design some Business Cards

Brelland Capital Pty Ltd

We are a commercial finance brokerage company based in Australia. We need a creative graphic designer to design business cards for us.

What we need for the business cards are,

1. Simple and professional.

2. Content will have our company name, employer name, position title, Telephone number, mobile number, email, company address, website and ACL (Australian Credit Licence Number), we have three people in our company so we need three files and one template for future use.

3. attached is our company logo with different colour. More format could be provided upon request.

Please lodge your entry if you are really a creative and professional designer.

Thanks.

```html
<!DOCTYPE html>
<html lang="en">
<head>
<meta charset="utf-8">
<title>Brelland Capital — Business Cards</title>
<link href="https://fonts.googleapis.com/css2?family=Tinos:ital,wght@0,400;0,700;1,400&display=swap" rel="stylesheet">
<style>
  :root {
    --backdrop: #5b5b5b;
    --card: #ffffff;
    --ink: #1c1c1c;
    --ink-soft: #3a3a3a;
  }
  html, body {
    margin: 0;
    width: 1200px;
    height: 900px;
    overflow: hidden;
    background: var(--backdrop);
    font-family: "Tinos", "Times New Roman", serif;
    color: var(--ink);
  }
  .stage { position: relative; width: 1200px; height: 900px; }
  .card {
    position: absolute;
    width: 540px;
    height: 310px;
    background: var(--card);
    border-radius: 30px;
    box-shadow: 0 14px 30px rgba(0,0,0,.35);
  }
  .card-front { left: 110px; top: 110px; }
  .card-back { left: 550px; top: 480px; }

  .front-wordmark {
    position: absolute;
    left: 0; right: 0; top: 50%;
    transform: translateY(-50%);
    text-align: center;
    font-size: 46px;
    letter-spacing: 7px;
    font-weight: 400;
  }

  .back-wordmark {
    position: absolute;
    left: 36px; top: 52px;
    font-size: 17px;
    letter-spacing: 3px;
  }
  .company-block {
    position: absolute;
    right: 36px; top: 44px;
    font-size: 10px;
    line-height: 1.35;
    text-align: left;
  }
  .company-block .licence { font-weight: 700; }

  .person {
    position: absolute;
    left: 70px; top: 184px;
    font-size: 10px;
    line-height: 1.35;
  }
  .person-name { font-weight: 700; font-size: 11px; letter-spacing: .5px; }
  .person-role { color: var(--ink-soft); }
  .rule { display: block; width: 14px; height: 1px; background: var(--ink); margin: 6px 0 4px; }
  .address { font-style: italic; }
  .phones .label { font-weight: 700; display: inline-block; width: 14px; }

  .online {
    position: absolute;
    left: 290px; top: 214px;
    font-size: 10px;
    line-height: 1.35;
  }
  .online .label { font-weight: 700; display: inline-block; width: 16px; }
</style>
</head>
<body>
<main class="stage">
  <section class="card card-front">
    <div class="front-wordmark">BRELLAND</div>
  </section>

  <section class="card card-back">
    <div class="back-wordmark">BRELLAND</div>

    <div class="company-block">
      <div>Brelland Capital Pty Ltd</div>
      <div class="licence">ACL:0487216350</div>
    </div>

    <div class="person">
      <div class="person-name">MARCUS HALE</div>
      <div class="person-role">Managing Director</div>
      <span class="rule"></span>
      <div class="address">42 Kestrel Lane, Parramatta<br>Australia, 2150</div>
      <span class="rule"></span>
      <div class="phones">
        <div><span class="label">T:</span> 02-8471-3306</div>
        <div><span class="label">M:</span> 0412-958-204</div>
      </div>
    </div>

    <div class="online">
      <div><span class="label">E:</span> marcus@brellandcap.com.au</div>
      <div><span class="label">W:</span> www.brellandcap.com.au</div>
    </div>
  </section>
</main>
</body>
</html>
```